Plakat für Verein
Zielgruppe
Wir möchten eine Veranstaltung für unseren Verein - Hinterbrunnthaler Nachbarschaftsbund machen.
Aufgabenstellung
Die Party der Golden 20er
Glanz-Glamour-Lebenslust
Tanzen wie früher - Feiern wie nie
21. März - Uhrzeit: 20.30 im Saal KW
Live mit DJaneMarlies
Dresscode: Goldene 20er - Fransen, Federn, Hosenträger, Zylinder
Farbe: Gold/Schgwarz

```html
<!DOCTYPE html>
<html lang="de">
<head>
<meta charset="utf-8">
<title>Die Party der Golden 20er – Plakat</title>
<link rel="stylesheet" href="https://fonts.googleapis.com/css2?family=Limelight&family=Poiret+One&family=Raleway:wght@300;700;800&display=swap">
<style>
  :root {
    --ink: #ffffff;
    --night: #060504;
    --smoke: #1a1712;
    --champagne: #8a6c45;
    --glow: #cfc8bc;
  }
  html, body {
    margin: 0;
    padding: 0;
    width: 849px;
    height: 1200px;
    overflow: hidden;
    background: var(--night);
  }
  .poster {
    position: relative;
    width: 849px;
    height: 1200px;
    overflow: hidden;
    color: var(--ink);
    font-family: "Poiret One", sans-serif;
  }
  .poster p { margin: 0; }
  .poster__photo {
    position: absolute;
    inset: 0;
    background:
      radial-gradient(ellipse 60px 60px at 615px 490px, rgba(207,200,188,.55), transparent 100%),
      radial-gradient(ellipse 70px 75px at 395px 415px, rgba(207,200,188,.5), transparent 100%),
      radial-gradient(ellipse 65px 70px at 800px 490px, rgba(207,200,188,.45), transparent 100%),
      radial-gradient(ellipse 75px 80px at 405px 615px, rgba(207,200,188,.45), transparent 100%),
      radial-gradient(ellipse 85px 85px at 150px 630px, rgba(138,108,69,.45), transparent 100%),
      radial-gradient(ellipse 90px 260px at 490px 920px, rgba(138,108,69,.55), transparent 100%),
      linear-gradient(180deg, var(--night) 0%, var(--smoke) 45%, var(--night) 100%);
  }
  .tagline {
    position: absolute;
    top: 14px;
    left: 0;
    width: 100%;
    text-align: center;
    font-size: 32px;
    white-space: nowrap;
    -webkit-text-stroke: .8px var(--ink);
  }
  .title {
    position: absolute;
    top: 58px;
    left: 0;
    width: 100%;
    margin: 0;
    text-align: center;
    font-family: "Limelight", "Poiret One", sans-serif;
    font-weight: 400;
    font-size: 92px;
    line-height: 99px;
    letter-spacing: 2px;
    white-space: nowrap;
  }
  .slogan {
    position: absolute;
    top: 258px;
    left: 0;
    width: 100%;
    text-align: center;
    font-size: 54px;
    white-space: nowrap;
    -webkit-text-stroke: 1.4px var(--ink);
  }
  .act {
    position: absolute;
    top: 490px;
    left: 46px;
    font-size: 46px;
    white-space: nowrap;
    -webkit-text-stroke: 2px var(--ink);
  }
  .details {
    position: absolute;
    right: 33px;
    top: 1110px;
    text-align: right;
    font-family: "Raleway", sans-serif;
    white-space: nowrap;
  }
  .details__when {
    font-weight: 800;
    font-size: 28px;
    line-height: 34px;
  }
  .details__dresscode {
    font-weight: 300;
    font-size: 17px;
    line-height: 22px;
  }
  .club {
    position: absolute;
    left: 16px;
    bottom: 22px;
    width: 200px;
    text-align: center;
    font-family: "Raleway", sans-serif;
    font-weight: 700;
    font-size: 15px;
    line-height: 22px;
    white-space: nowrap;
  }
  .club__dot {
    display: block;
    width: 28px;
    height: 28px;
    margin: 0 auto 16px;
    border-radius: 50%;
    background: var(--ink);
  }
</style>
</head>
<body>
<main class="poster">
  <div class="poster__photo" role="img" aria-label="Sektglas mit Champagner vor dunklem Hintergrund mit warmen, unscharfen Lichtpunkten"></div>

  <p class="tagline">Tanzen wie früher – Feiern wie nie!</p>
  <h1 class="title">DIE PARTY DER<br>GOLDEN 20ER</h1>
  <p class="slogan">Glanz – Glamour – Lebenslust</p>

  <p class="act">Live mit DJane Marlies</p>

  <div class="club">
    <span class="club__dot"></span>
    HINTERBRUNNTHALER<br>NACHBARSCHAFTSBUND
  </div>

  <div class="details">
    <div class="details__when">21. MÄRZ – UHRZEIT: 20:30 IM SAAL KW</div>
    <div class="details__dresscode">Dresscode: Goldene 20er – Fransen, Federn, Hosenträger, Zylinder</div>
  </div>
</main>
</body>
</html>
```